KINDLEA: Flu Social Media Post #2

- Please create a similar design to the one attached to create a Social Media Post image.
- Attached, Logo, boarder, sample flu social media image.
- KINDLEA - must be included
- Flu - must be included
- Protect your community. Protect Your Elders. Stay Vaccinated. - must be included
- image of mom/daughter holding hands must be included
- For inspiration, https://brovelink.example/, and https://www.facebook.com/Brovelink

```html
<!DOCTYPE html>
<html lang="en">
<head>
<meta charset="utf-8">
<title>KINDLEA – Flu Social Media Post</title>
<link href="https://fonts.googleapis.com/css2?family=Barlow+Semi+Condensed:wght@500;600&family=Overpass:wght@900&display=swap" rel="stylesheet">
<style>
  :root {
    --cream: #fdf0dc;
    --teal: #4aa3ac;
    --brick: #b5554d;
    --band: rgba(255, 255, 255, 0.72);
    --frame-a: #5fa9b0;
    --frame-b: #9e6a66;
    --white: #ffffff;
  }
  html, body {
    margin: 0;
    padding: 0;
    width: 1200px;
    height: 1200px;
    overflow: hidden;
    background: var(--white);
  }
  .post {
    position: relative;
    width: 1200px;
    height: 1200px;
    overflow: hidden;
  }
  .frame-pattern {
    position: absolute;
    inset: 0;
    background: linear-gradient(135deg, var(--frame-a), #c9d6d6 50%, var(--frame-b));
  }
  .panel {
    position: absolute;
    left: 37px;
    top: 37px;
    width: 1126px;
    height: 1126px;
    background: var(--cream);
    overflow: hidden;
  }
  .photo {
    position: absolute;
    left: 13px;
    top: 453px;
    width: 1113px;
    height: 673px;
    background: linear-gradient(90deg,
      rgba(110, 40, 80, 0.85) 0%,
      rgba(70, 40, 60, 0.8) 30%,
      rgba(253, 240, 220, 0.2) 50%,
      rgba(30, 25, 25, 0.85) 70%,
      rgba(40, 30, 35, 0.9) 100%);
  }
  .headline-box {
    position: absolute;
    left: 46px;
    top: 46px;
    width: 774px;
    height: 174px;
    border: 6px solid var(--teal);
    box-sizing: border-box;
    display: flex;
    align-items: center;
    justify-content: center;
  }
  .headline {
    margin: 0;
    font-family: "Barlow Semi Condensed", sans-serif;
    font-weight: 500;
    font-size: 168px;
    line-height: 1;
    letter-spacing: 8px;
    color: var(--brick);
    padding-top: 6px;
  }
  .brand {
    position: absolute;
    left: 857px;
    top: 100px;
    width: 220px;
    display: flex;
    align-items: center;
    gap: 10px;
  }
  .brand-mark {
    width: 34px;
    height: 34px;
    background: var(--teal);
    flex: none;
  }
  .brand-name {
    font-family: "Barlow Semi Condensed", sans-serif;
    font-weight: 600;
    font-size: 26px;
    line-height: 1.1;
    color: var(--teal);
    text-transform: uppercase;
  }
  .band {
    position: absolute;
    left: 0;
    width: 100%;
    height: 110px;
    background: var(--band);
  }
  .band-1 { top: 265px; }
  .band-2 { top: 516px; }
  .band-3 { top: 759px; }
  .message {
    position: absolute;
    left: 0;
    width: 100%;
    margin: 0;
    text-align: center;
    font-family: "Overpass", sans-serif;
    font-weight: 900;
    font-size: 98px;
    line-height: 1;
    letter-spacing: 2px;
    transform: translateY(-50%);
  }
  .message.teal { color: var(--teal); }
  .message.brick {
    color: var(--brick);
    text-shadow: 0 0 6px var(--white), 0 0 3px var(--white);
  }
  .line-1 { top: 324px; }
  .line-2 { top: 430px; }
  .line-3 { top: 584px; }
  .line-4 { top: 692px; }
  .line-5 { top: 817px; }
  .line-6 { top: 924px; }
  .cta-bar {
    position: absolute;
    left: -4px;
    top: 994px;
    width: 1132px;
    height: 90px;
    background: var(--white);
    box-shadow: 0 2px 6px rgba(0,0,0,0.15);
    display: flex;
    align-items: center;
    justify-content: center;
  }
  .cta {
    margin: 0;
    font-family: "Barlow Semi Condensed", sans-serif;
    font-weight: 500;
    font-size: 44px;
    letter-spacing: 2px;
    color: var(--teal);
  }
</style>
</head>
<body>
  <main class="post">
    <div class="frame-pattern" role="img" aria-label="Woven zigzag border pattern in teal, grey and rose"></div>
    <section class="panel">
      <div class="photo" role="img" aria-label="Mother and daughter seen from behind, holding hands, wearing embroidered traditional blouses"></div>

      <div class="headline-box">
        <h1 class="headline">KINDLEA</h1>
      </div>

      <div class="brand">
        <span class="brand-mark"></span>
        <span class="brand-name">Brovelink Elder Network</span>
      </div>

      <div class="band band-1"></div>
      <div class="band band-2"></div>
      <div class="band band-3"></div>

      <p class="message teal line-1">Protect Your</p>
      <p class="message brick line-2">Community</p>
      <p class="message teal line-3">Protect Your</p>
      <p class="message brick line-4">Elders</p>
      <p class="message teal line-5">Stay</p>
      <p class="message brick line-6">Vaccinated</p>

      <div class="cta-bar">
        <p class="cta">Learn more about getting vaccinated against the Flu</p>
      </div>
    </section>
  </main>
</body>
</html>
```